Ned Halvorsen Executive Coach Business Card Design

I need a new card design for my Executive Coaching practice. I am a Clinical Psychotherapist and Executive Coach. I help my clients get the most out of life by developing their personal and professional skills and abilities.

I work with senior executives. My design needs to be high end. I am thinking gloss on the front. I am also thinking contemporary. I am going to use a black, grey and red colour scheme on the the website. I am thinking grey with black and red accents. I would also like a water mark included on the card.

Target Market(s)

Senior Executives In major Companies

Industry/Entity Type

Business

Contact Information for Business Card

On the front

Ned Halvorsen
Clinical Psychotherapist and Executive Coach
For Personal and Professional Success

On the Back

Tarrant office
87 Tarrant Vale Road Tarrant

North Sydney Office
Suite 309 / 41 Pellow Street North Sydney

Danforth Street Office
Suite 512 / 248 Danforth Street Sydney CBD

Phone 02 95517384
Email ned@nedhalvorsen.example.au

Requirements
Must have
• Friendly but professional
Water Mark
Gloss Front

```html
<!DOCTYPE html>
<html lang="en">
<head>
<meta charset="utf-8">
<title>Ned Halvorsen – Business Card</title>
<link rel="stylesheet" href="https://fonts.googleapis.com/css2?family=Mulish:wght@300;400;500&display=swap">
<style>
  :root {
    --backdrop: #3b3531;
    --card-light: #f4f4f4;
    --card-mid: #dcdcdc;
    --card-dark: #c9c9c9;
    --ink: #1d1d1d;
    --ink-soft: #3a3a3a;
    --accent-red: #c2353b;
    --paper-white: #ffffff;
    --pale-type: #f1f1f1;
  }
  * { box-sizing: border-box; margin: 0; padding: 0; }
  html, body {
    width: 1200px; height: 794px; overflow: hidden;
    background: var(--backdrop);
    font-family: "Mulish", "Helvetica Neue", Arial, sans-serif;
  }
  .stage {
    position: relative; width: 1200px; height: 794px;
    display: flex; align-items: center; justify-content: center; gap: 60px;
  }
  .card {
    position: relative; width: 490px; height: 280px;
    border-radius: 3px; overflow: hidden;
    box-shadow: 0 10px 30px rgba(0,0,0,.45);
  }
  .card--front {
    background: linear-gradient(160deg, var(--card-light) 0%, var(--card-mid) 55%, var(--card-dark) 100%);
  }
  .card--front::after {
    content: ""; position: absolute; inset: 0; pointer-events: none;
    background: linear-gradient(115deg, rgba(255,255,255,.55) 0%, rgba(255,255,255,0) 40%);
  }
  .card--back {
    background: linear-gradient(160deg, #ececec 0%, var(--card-mid) 60%, #d2d2d2 100%);
  }
  .front-name {
    position: absolute; left: 26px; top: 150px;
    font-size: 31px; font-weight: 400; letter-spacing: .5px; line-height: 1.2;
    color: var(--ink); text-transform: uppercase; white-space: nowrap;
  }
  .front-role {
    position: absolute; left: 27px; top: 189px;
    font-size: 12.5px; font-weight: 400; color: var(--ink-soft); white-space: nowrap;
  }
  .rule {
    position: absolute; left: 26px; right: 26px; height: 1px;
    background: var(--accent-red); z-index: 2;
  }
  .front-rule { top: 210px; }
  .front-tagline {
    position: absolute; left: 26px; top: 222px;
    font-size: 17.5px; font-weight: 300; letter-spacing: 1.4px;
    color: var(--pale-type); text-transform: uppercase; white-space: nowrap;
    text-shadow: 0 0 1px rgba(0,0,0,.12);
  }
  .back-watermark {
    position: absolute; left: 22px; top: 22px;
    font-size: 46px; font-weight: 300; letter-spacing: 1px; line-height: 1.2;
    color: var(--paper-white); text-transform: uppercase; white-space: nowrap;
    text-shadow: 0 1px 1px rgba(0,0,0,.12);
  }
  .back-services {
    position: absolute; left: 24px; top: 90px;
    font-size: 13px; font-weight: 400; line-height: 1.5;
    color: var(--paper-white); white-space: nowrap;
    text-shadow: 0 0 1px rgba(0,0,0,.15);
  }
  .dot { margin: 0 6px; }
  .back-rule { top: 142px; }
  .back-contact {
    position: absolute; left: 24px; top: 156px;
    display: flex; gap: 22px;
    font-size: 11.5px; color: var(--ink); align-items: center; white-space: nowrap;
  }
  .contact-item { display: flex; align-items: center; gap: 6px; }
  .contact-item svg { width: 12px; height: 12px; fill: var(--ink); }
  .back-offices {
    position: absolute; left: 24px; top: 182px;
    list-style: none; font-size: 11px; line-height: 1.75; color: var(--ink); white-space: nowrap;
  }
</style>
</head>
<body>
<main class="stage">
  <section class="card card--front" aria-label="Card front">
    <h1 class="front-name">Ned Halvorsen</h1>
    <p class="front-role">Clinical Psychotherapist and Executive Coach</p>
    <div class="rule front-rule"></div>
    <p class="front-tagline">For Personal and Professional Success</p>
  </section>

  <section class="card card--back" aria-label="Card back">
    <p class="back-watermark">Ned Halvorsen</p>
    <p class="back-services">
      Clinical Psychotherapy<span class="dot">•</span>Executive Coaching and Mentoring<br>
      Professional Development Training<span class="dot">•</span>Team Building
    </p>
    <div class="rule back-rule"></div>
    <div class="back-contact">
      <span class="contact-item">
        <svg viewBox="0 0 24 24" aria-hidden="true"><path d="M6.6 10.8a15.1 15.1 0 0 0 6.6 6.6l2.2-2.2a1 1 0 0 1 1-.25 11.4 11.4 0 0 0 3.6.57 1 1 0 0 1 1 1V20a1 1 0 0 1-1 1A17 17 0 0 1 3 4a1 1 0 0 1 1-1h3.5a1 1 0 0 1 1 1c0 1.25.2 2.450.57 3.57a1 1 0 0 1-.25 1z"/></svg>
        02 95 517 384
      </span>
      <span class="contact-item">
        <svg viewBox="0 0 24 24" aria-hidden="true"><path d="M2 5h20v14H2z M4 7v.4l8 5.2 8-5.2V7z" fill-rule="evenodd"/></svg>
        ned@nedhalvorsen.example.au
      </span>
    </div>
    <ul class="back-offices">
      <li>Tarrant Office: 87 Tarrant Vale Road Tarrant NSW 2037</li>
      <li>North Sydney Office: Suite 309 / 41 Pellow Street North Sydney NSW 2060</li>
      <li>Danforth Street Office: Suite 512 / 248 Danforth Street Sydney CBD NSW 2000</li>
    </ul>
  </section>
</main>
</body>
</html>
```